Sales Process Flyer

Attached is a sketch (2 pages) Id like to have a 1 page "flyer" that will explain the sales strategy for a new recruit.
Ill need to edit this down the road, so if you do it in Illustrator we will be able to handle that.
If you plenvo sales funnel you will see what im going for with the bad funnel drawing.
Id like to have icons with the text thats on the 2nd page (although it would all be 1 page)
Our brand guidelines are attached with some example pieces we have done in the past
Would like this to have an infographic type look

Something I didnt work in the sketch is below.
Estimated Sales Time:
25% - Meeting & Managing Existing Clients
25% - Free Assessments & Proposals
25% - Cold Calling
25% - New Customer Meetings & Networking

Plenvo

```html
<!DOCTYPE html>
<html lang="en">
<head>
<meta charset="utf-8">
<title>Sales Strategy</title>
<link rel="stylesheet" href="https://fonts.googleapis.com/css2?family=Dosis:wght@400;500;600&family=Open+Sans:wght@600;700&display=swap">
<style>
  :root {
    --slate: #5d5e60;
    --brand-blue: #0a7ca8;
    --text-blue: #1d7ea8;
    --bar-grey: #a6a7a9;
    --panel: #dfe3e4;
    --white: #ffffff;
    --step-1: #c9cccd;
    --step-2: #b9bcbd;
    --step-3: #aeb1b2;
    --step-4: #9c9ea0;
    --step-5: #818284;
    --light-blue: #35b9e9;
  }
  * { box-sizing: border-box; margin: 0; padding: 0; }
  html, body { width: 927px; height: 1200px; overflow: hidden; }
  body { background: var(--slate); position: relative; font-family: "Open Sans", Arial, sans-serif; }

  .top-band { position: absolute; left: 0; top: 42px; width: 927px; height: 59px; background: var(--brand-blue); }
  .title { position: absolute; left: 237px; top: 48px; font-family: "Dosis", sans-serif; font-weight: 500; font-size: 36px; letter-spacing: 7px; color: var(--white); }
  .brand-mark { position: absolute; left: 110px; top: 28px; width: 90px; height: 90px; border-radius: 50%; background: var(--white); }
  .brand-mark .mark-fill { position: absolute; left: 20px; top: 26px; width: 50px; height: 38px; border-radius: 50%; background: var(--slate); }

  .sheet { position: absolute; left: 44px; top: 130px; width: 849px; height: 1031px; background: var(--white); }
  .sheet-foot { position: absolute; left: 0; bottom: 0; width: 100%; height: 18px; background: var(--brand-blue); }

  .pillars { position: absolute; left: 0; top: 1px; width: 100%; height: 63px; background: var(--bar-grey); }
  .pillar { position: absolute; top: 14px; display: flex; align-items: center; gap: 12px; font-family: "Dosis", sans-serif; font-weight: 500; font-size: 30px; color: var(--white); letter-spacing: 0.5px; }
  .pillar::before { content: ""; width: 30px; height: 30px; border-radius: 50%; background: var(--brand-blue); }

  .funnel-panel { position: absolute; left: 31px; top: 82px; width: 789px; height: 539px; background: var(--panel); border-radius: 18px; }
  .step { position: absolute; left: 28px; width: 347px; display: flex; flex-direction: column; justify-content: center; padding-left: 24px; border-radius: 3px; font-weight: 700; font-size: 13.5px; line-height: 18px; color: var(--text-blue); }
  .step ul { list-style: none; }
  .step li::before { content: "\2022"; margin-right: 8px; }
  .step .note { padding-left: 22px; font-size: 12.5px; }
  .step.light { color: var(--light-blue); }

  .funnel { position: absolute; left: 0; top: 0; }
  .funnel text { font-family: "Open Sans", sans-serif; font-weight: 700; font-size: 13px; fill: var(--white); text-anchor: middle; }

  .won { position: absolute; left: 613px; top: 417px; font-family: "Dosis", sans-serif; font-weight: 600; font-size: 30px; color: var(--brand-blue); }

  .lost-bar { position: absolute; left: 74px; top: 465px; width: 616px; height: 54px; background: #999a9c; border-radius: 3px; font-family: "Dosis", sans-serif; font-weight: 500; font-size: 22px; color: var(--white); white-space: nowrap; }
  .lost-bar .lost { position: absolute; left: 0; top: 0; width: 135px; height: 54px; background: var(--brand-blue); border-radius: 3px; display: flex; align-items: center; justify-content: center; font-size: 28px; }
  .lost-bar span { position: absolute; top: 13px; transform: translateX(-50%); }

  .channels { position: absolute; left: 31px; top: 642px; width: 410px; height: 340px; background: var(--panel); border-radius: 16px; }
  .channel { position: absolute; left: 12px; display: flex; align-items: center; gap: 14px; font-weight: 700; font-size: 14.5px; line-height: 20px; color: var(--text-blue); }
  .channel .tile { width: 48px; height: 48px; flex: none; border-radius: 6px; background: var(--brand-blue); display: flex; align-items: center; justify-content: center; }
  .channel .name-tag { width: 110px; flex: none; display: flex; align-items: center; gap: 6px; }
  .channel .name-tag i { width: 14px; height: 14px; background: var(--brand-blue); display: block; }
  .channel small { font-size: 10px; }

  .sales-time { position: absolute; left: 467px; top: 643px; width: 358px; height: 339px; background: var(--panel); border-radius: 16px; overflow: hidden; }
  .sales-time h2 { height: 66px; background: var(--bar-grey); border-radius: 16px 16px 0 0; font-family: "Dosis", sans-serif; font-weight: 500; font-size: 28px; color: var(--white); display: flex; align-items: center; justify-content: center; }
  .sales-time .share { position: absolute; left: 38px; top: 68px; width: 320px; font-family: "Dosis", sans-serif; font-weight: 500; font-size: 190px; line-height: 1; color: var(--white); letter-spacing: 4px; white-space: nowrap; }
  .sales-time ul { position: absolute; left: 19px; top: 88px; list-style: none; font-family: "Dosis", sans-serif; font-weight: 600; font-size: 20px; color: var(--text-blue); white-space: nowrap; }
  .sales-time li { height: 54.5px; }
</style>
</head>
<body>
  <div class="top-band"></div>
  <div class="brand-mark"><div class="mark-fill" role="img" aria-label="Company mascot mark"></div></div>
  <h1 class="title">SALES STRATEGY</h1>

  <main class="sheet">
    <div class="pillars">
      <div class="pillar" style="left:90px">STRATEGY</div>
      <div class="pillar" style="left:368px">EFFORT</div>
      <div class="pillar" style="left:614px">SKILL</div>
    </div>

    <section class="funnel-panel">
      <div class="step" style="top:26px;height:75px;background:var(--step-1)">
        <ul><li>Landing page created on website</li><li>Specific email crafted</li><li>500 emails sent</li></ul>
      </div>
      <div class="step" style="top:106px;height:67px;background:var(--step-2)">
        <ul><li>Phone call follow up with click's</li><li>Phone call follow up with opens</li><li>Phone call follow up with remaining</li></ul>
        <div class="note">* Make free assesmnet pitch</div>
      </div>
      <div class="step" style="top:181px;height:70px;background:var(--step-3)"><ul><li>Run free assesment</li></ul></div>
      <div class="step light" style="top:259px;height:65px;background:var(--step-4)"><ul><li>Meeting schedule</li></ul></div>
      <div class="step light" style="top:335px;height:64px;background:var(--step-5);left:26px"><ul><li>Proposal</li></ul></div>

      <svg class="funnel" width="789" height="539" viewBox="0 0 789 539">
        <defs><marker id="head" markerWidth="10" markerHeight="8" refX="9" refY="4" orient="auto"><path d="M0 0L10 4L0 8z" fill="#111"/></marker></defs>
        <g stroke="#111" stroke-width="1.5" marker-end="url(#head)">
          <line x1="394" y1="57" x2="470" y2="57"/>
          <line x1="399" y1="139" x2="474" y2="139"/>
          <line x1="399" y1="216" x2="475" y2="216"/>
          <line x1="401" y1="291" x2="477" y2="291"/>
          <line x1="405" y1="367" x2="480" y2="367"/>
        </g>
        <path d="M470 31 L707 31 L694 101 L482 101 Z" fill="#136c86"/>
        <ellipse cx="588" cy="31" rx="118" ry="9" fill="#a7a9ab"/>
        <ellipse cx="588" cy="101" rx="106" ry="6" fill="#136c86"/>
        <path d="M476 106 L702 106 L688 173 L488 173 Z" fill="#8d5f42"/>
        <ellipse cx="589" cy="106" rx="113" ry="8" fill="#a7a9ab"/>
        <ellipse cx="588" cy="173" rx="100" ry="6" fill="#8d5f42"/>
        <path d="M482 181 L696 181 L684 251 L494 251 Z" fill="#0f87ae"/>
        <ellipse cx="589" cy="181" rx="107" ry="8" fill="#a7a9ab"/>
        <ellipse cx="589" cy="251" rx="95" ry="6" fill="#0f87ae"/>
        <path d="M488 259 L691 259 L679 325 L500 325 Z" fill="#d98c5f"/>
        <ellipse cx="589" cy="259" rx="101" ry="7" fill="#a7a9ab"/>
        <ellipse cx="589" cy="325" rx="89" ry="6" fill="#d98c5f"/>
        <path d="M495 335 L685 335 L673 400 L506 400 Z" fill="#5aa06a"/>
        <ellipse cx="590" cy="335" rx="95" ry="7" fill="#a7a9ab"/>
        <ellipse cx="589" cy="400" rx="83" ry="6" fill="#5aa06a"/>
        <text x="589" y="60">5% email sent</text>
        <text x="589" y="133">10% first contacts</text><text x="589" y="165">180 goal</text>
        <text x="589" y="209">25% assesment</text><text x="589" y="240">60 goal</text>
        <text x="589" y="284">50% meeting</text><text x="589" y="315">32 goal</text>
        <text x="589" y="359">75% proposal</text><text x="589" y="390">16 goal</text>
        <path d="M585 410 L591 428 L610 428 L595 439 L601 457 L585 446 L569 457 L575 439 L560 428 L579 428 Z" fill="var(--brand-blue)"/>
      </svg>
      <div class="won">WON</div>

      <div class="lost-bar">
        <div class="lost">LOST</div>
        <span style="left:201px">PRICE</span>
        <span style="left:355px">TIME LINE</span>
        <span style="left:526px">UNKWON</span>
      </div>
    </section>

    <section class="channels">
      <div class="channel" style="top:12px"><div class="name-tag"><i></i>Blogly</div><div>4 post per month<br>on industry specific topic</div></div>
      <div class="channel" style="top:66px"><div class="name-tag"><i></i>Linkora</div><div>1 hour per week<br>prospecting and connecting</div></div>
      <div class="channel" style="top:128px"><div class="name-tag"><i></i>Friendra</div><div>4 events per month</div></div>
      <div class="channel" style="top:172px"><div class="tile"><svg width="30" height="24" viewBox="0 0 30 24"><rect x="1" y="1" width="28" height="22" rx="2" fill="#fff"/><g stroke="#0a7ca8" stroke-width="2"><line x1="6" y1="7" x2="24" y2="7"/><line x1="6" y1="12" x2="24" y2="12"/><line x1="6" y1="17" x2="16" y2="17"/></g></svg></div><div>1 hour per week <small>(account management)</small><br>checking with previous clients</div></div>
      <div class="channel" style="top:228px"><div class="tile"><svg width="30" height="24" viewBox="0 0 30 24"><rect x="1" y="1" width="28" height="22" rx="2" fill="#fff"/><polyline points="4,14 10,14 13,6 17,19 20,10 26,10" fill="none" stroke="#0a7ca8" stroke-width="2"/></svg></div><div>Trade Show<br>1 per month</div></div>
      <div class="channel" style="top:283px"><div class="tile"><svg width="30" height="24" viewBox="0 0 30 24"><rect x="3" y="3" width="24" height="16" rx="3" fill="#fff"/></svg></div><div>Ask for referals generate<br>1 referral per week</div></div>
    </section>

    <section class="sales-time">
      <h2>ESTIMATED SALES TIME</h2>
      <div class="share" aria-hidden="true">25 %</div>
      <ul>
        <li>Meeting &amp; Managing Existing Clients</li>
        <li>Free Assessments &amp; Proposals</li>
        <li>Cold Calling</li>
        <li>New Customer Meetings &amp; Networking</li>
      </ul>
    </section>

    <div class="sheet-foot"></div>
  </main>
</body>
</html>
```